Frontpage for an independent Forex trading tournaments website

We need a frontpage design for the first independent Forex trading tournaments platform.
Intraday Forex traders from all over the world come to this website to participate in daily contests, and if they trade better than others — win the bets. This website is the first of a kind — it is not affiliated with any type of brokers, and does not promote any broker services.
People can trade with their existing live or demo accounts (and they even can win real money with demo accounts)
The main goal of the frontpage is to explain what this website is about and make them sign up via Chatterloop or Quipster buttons, or traditional email.
Attached to this project is a sample mock-up that seems reasonable, but we're open to further suggestions.
Updates
Dear designers,
Also please use bigger fonts and use don't leave too big blank spaces.
Target Market(s)
Intraday Forex traders from 24 to 34 years, mostly males, higher education, working as traders or trading as a hobby.
Mostly living in developing countries: Indonesia, Eastern Europe, Arab countries, China, Latin America.
Industry/Entity Type
Trade
Requirements
Must have
- * Clean design with clear message
* An easy-to-see way to show that we have single-click Chatterloop/Quipster registration
Should not have
- * No implied javascript-animated nested menus or pop-ups, no flash — that would make the website difficult to browse on mobile devices which employ touch-based controls

```html
<!DOCTYPE html>
<html lang="en">
<head>
<meta charset="utf-8">
<title>TradeNova.com — Forex Trading Tournaments</title>
<link rel="stylesheet" href="https://fonts.googleapis.com/css2?family=Ubuntu:wght@400;500;700&display=swap">
<style>
:root{
  --bg:#0b0b0b;
  --bg-top:#1d1d1d;
  --footer:#070707;
  --gold:#f3a40c;
  --gold-light:#ffc230;
  --orange:#e88a0a;
  --red:#d11a12;
  --red-dark:#a10d08;
  --text:#d9d9d9;
  --muted:#b0b0b0;
  --row:#2a2a2a;
  --row-alt:#222;
  --line:#3c3c3c;
  --chat:#2f5aa6;
  --quip:#2aa3e6;
  --grey-btn:#4a4a4a;
}
*{margin:0;padding:0;box-sizing:border-box}
html,body{width:720px;height:1200px;overflow:hidden}
body{background:var(--bg);font-family:"Ubuntu",sans-serif;color:var(--text);position:relative}
.page{position:relative;width:720px;height:1200px;background:linear-gradient(#1c1c1c 0,#0e0e0e 80px,#0b0b0b 480px,#161616 860px)}
.abs{position:absolute}

/* header */
.topline{left:0;top:0;width:720px;height:3px;background:var(--gold)}
.signin-tab{left:594px;top:0;width:60px;height:20px;background:var(--gold);border-radius:0 0 8px 8px;font-size:10px;color:#1a1a1a;text-align:center;line-height:19px;text-decoration:underline}
.brand{left:84px;top:22px;font-size:34px;font-weight:500;color:#f2f2f2;letter-spacing:-1px}
.brand .star{color:var(--gold)}
.nav a{position:absolute;top:37px;font-size:10.5px;color:var(--gold);text-decoration:underline}
.join-btn{left:599px;top:30px;width:53px;height:25px;background:linear-gradient(#e02217,var(--red-dark));border-radius:2px;color:#fff;font-size:10.5px;text-align:center;line-height:25px;text-decoration:underline}

.headline{left:0;top:73px;width:720px;text-align:center;font-size:17.5px;font-weight:500;color:var(--gold);line-height:21px}

/* hero */
.hero{left:77px;top:128px;width:566px;height:246px;border:6px solid var(--orange);background:#3a1d07}
.hero-photo{position:absolute;inset:0;background:linear-gradient(100deg,#5e3512 0%,#3b2410 35%,#2a1a0e 55%,#6e3a10 85%,#8a4a12 100%)}
.quote{position:absolute;left:248px;top:93px;width:307px;height:124px;background:rgba(6,6,6,.93);padding:21px 25px;font-size:12.6px;line-height:14.5px;color:#e6e6e6}

/* brokers */
.brokers{left:78px;top:388px;width:565px;height:70px;background:#fbfbfb;border-radius:3px}
.brokers h2{position:absolute;left:15px;top:10px;font-size:15.5px;font-weight:500;color:#3a3a3a}
.pager{position:absolute;top:10px;width:8px;height:8px;border-radius:50%;background:#ddd}
.broker{position:absolute;top:40px;font-size:11px;color:#333;display:flex;align-items:center;gap:4px;white-space:nowrap}
.broker i{display:inline-block;width:11px;height:11px;background:#c8241c}

.section-title{left:0;top:478px;width:720px;text-align:center;font-size:16px;color:var(--gold)}

/* tournaments table */
.table{left:77px;top:509px;width:565px;height:271px;background:var(--row)}
.thead{position:absolute;left:0;top:0;width:565px;height:31px;background:linear-gradient(var(--gold-light),var(--orange));border-radius:3px 3px 0 0;font-size:15px;color:#fff}
.thead span,.row span{position:absolute}
.row{position:absolute;left:0;width:565px;height:28.5px;border-bottom:1px solid var(--line);font-size:10.5px;color:#e8e8e8}
.row span{top:8px}
.row .name{font-weight:500}
.c1{left:9px}.c2{left:193px}.c3{left:337px}.c4{left:456px}
.btn-join{position:absolute;left:457px;top:4px;width:65px;height:20px;border-radius:2px;background:linear-gradient(#e52a1f,var(--red-dark));color:#fff;font-size:10.5px;font-weight:500;text-align:center;line-height:20px}
.btn-join.gold{background:linear-gradient(var(--gold-light),#e08a08)}
.details{position:absolute;left:0;top:174px;width:565px;font-size:10px;color:#cfcfcf}
.details div{position:absolute;white-space:nowrap}
.details small{font-size:7px}
.rules{position:absolute;left:9px;top:245px;font-size:10.5px;font-weight:500;color:#e8e8e8;text-decoration:underline}

/* registration */
.badge{left:93px;top:791px;width:58px;height:58px;border-radius:50%;background:#f4f4ee;border:4px solid #3e9a2a}
.social-btn{top:806px;height:25px;border-radius:3px;font-size:8px;color:#fff;display:flex;align-items:center}
.social-btn .dot{width:27px;height:27px;border-radius:50%;background:#fff;margin-left:-2px;margin-right:9px;flex:none}
.chat{left:168px;width:126px;background:var(--chat)}
.chat .dot{background:#26498a;border:2px solid #5b82c8}
.quip{left:306px;width:127px;background:var(--quip)}
.quip .dot{background:#1e8fd0;border:2px solid #6cc3f0}
.or{left:452px;top:813px;font-size:10.5px;color:#ddd}
.email-btn{left:480px;top:805px;width:146px;height:27px;border-radius:2px;background:linear-gradient(#5a5a5a,#3a3a3a);font-size:7.5px;color:#eee;text-align:center;line-height:27px}

/* footer */
.footer{left:0;top:862px;width:720px;height:330px;background:var(--footer)}
.disclaimer-title{left:0;top:880px;width:720px;text-align:center;font-size:11.5px;color:#ddd}
.disclaimer{left:76px;top:902px;width:568px;text-align:center;font-size:7.2px;line-height:10.5px;color:#bdbdbd}
.links{top:968px;font-size:9px;line-height:21.6px}
.links a{display:block;color:#c9c9c9;text-decoration:underline}
.cards{left:69px;top:1126px;display:flex;gap:5px}
.cards span{width:21px;height:13px;background:#f5f5f5;border-radius:1px;font-size:4.5px;color:#1c3d8a;text-align:center;line-height:13px;font-weight:700}
.copyright{left:241px;top:1125px;font-size:8.5px;color:#aaa}
.langs{left:251px;top:1144px;font-size:8.5px;color:#aaa;letter-spacing:.3px}
.follow{left:554px;top:1129px;display:flex;gap:2px}
.follow span{width:21px;height:21px;border-radius:50%;border:1.5px solid #ccc}
.bottom-strip{left:0;top:1192px;width:720px;height:8px;background:#3a3a3a}
</style>
</head>
<body>
<div class="page">
  <div class="abs topline"></div>
  <a class="abs signin-tab">Sign In</a>
  <div class="abs brand">TradeNova<span class="star">.</span>com</div>
  <nav class="nav">
    <a style="left:403px">Tournaments</a>
    <a style="left:490px">Winners</a>
    <a style="left:558px">Q&amp;A</a>
  </nav>
  <a class="abs join-btn">Join</a>

  <h1 class="abs headline">Over 30,000 traders from all over theworld have joined PipArena.com<br>to participate in broker-independentreal -money forex tournaments</h1>

  <section class="abs hero">
    <div class="hero-photo" role="img" aria-label="Smiling young trader in a light blue shirt against a night city skyline"></div>
    <blockquote class="quote">I have beeen participating the tournaments for three months already,and I can't even find right words to express my passion for forex trading and excitement I get from fairly competing wih people who feel the same</blockquote>
  </section>

  <section class="abs brokers">
    <h2>BROKER TRUST US</h2>
    <span class="pager" style="left:535px"></span><span class="pager" style="left:547px"></span>
    <div class="broker" style="left:42px">Atlas Brokers</div>
    <div class="broker" style="left:132px"><i></i>Kestrel Bank</div>
    <div class="broker" style="left:236px">vantori</div>
    <div class="broker" style="left:296px;color:#3b8a2a">Lumex</div>
    <div class="broker" style="left:369px"><i style="background:#222"></i>Harbor Trading</div>
    <div class="broker" style="left:465px;font-size:13px"><i style="background:#8bc34a;border-radius:50%"></i>QUANTA</div>
  </section>

  <h2 class="abs section-title">SOONEST TOURNAMENTS</h2>

  <section class="abs table">
    <div class="thead"><span class="c1" style="top:8px">NAME</span><span class="c2" style="top:8px">DUE</span><span class="c3" style="top:8px">1ST PRIZE</span><span style="left:456px;top:8px">JOIN NOW</span></div>
    <div class="row" style="top:31px"><span class="c1 name">Double or  Nothing Thrity</span><span class="c2">in 24m</span><span class="c3">$ 60</span><a class="btn-join">$33</a></div>
    <div class="row" style="top:60px;background:var(--row-alt)"><span class="c1 name">Regular European Ten</span><span class="c2">in 4h 24m</span><span class="c3">$ 90</span><a class="btn-join gold">$11</a></div>
    <div class="row" style="top:89px"><span class="c1 name">Lucky European Freeoil</span><span class="c2">in 4h 24m</span><span class="c3">$ 15</span><a class="btn-join">FREE</a></div>
    <div class="row" style="top:117px;background:var(--row-alt)"><span class="c1 name">Regular American Ten</span><span class="c2">in 7h 24m</span><span class="c3">$100</span><a class="btn-join">$11</a></div>
    <div class="row" style="top:146px"><span class="c1 name">World Cup</span><span class="c2">in 3 months</span><span class="c3">$ 300 000</span><a class="btn-join">$100</a></div>
    <div class="details">
      <div style="left:9px;top:4px">Prize Fund</div><div style="left:82px;top:6px"><small>S 300 000</small></div>
      <div style="left:9px;top:26px">Participants</div><div style="left:82px;top:28px"><small>241 (max.10000)</small></div>
      <div style="left:9px;top:48px">Participants  Fee<small>$100</small></div>
      <div style="left:194px;top:4px">Registration Ends</div>
      <div style="left:194px;top:26px">Trading Starts</div>
      <div style="left:194px;top:48px">Trading Ends</div>
      <div style="left:338px;top:4px">15 Nov  2013,17:00 GMT</div>
      <div style="left:338px;top:26px">20 Dec  2013,17:00 GMT</div>
      <div style="left:338px;top:48px">20 Dec  2013,17:00 GMT</div>
    </div>
    <a class="rules">World Cup Tournament Rules</a>
  </section>

  <div class="abs badge" aria-hidden="true"></div>
  <a class="abs social-btn chat"><span class="dot"></span>ENTER WITH CHATTERLOOP</a>
  <a class="abs social-btn quip"><span class="dot"></span>ENTER WITH QUIPSTER</a>
  <span class="abs or">OR</span>
  <a class="abs email-btn">REGISTER WITH GOOD OLD EMAIL</a>

  <footer class="abs footer"></footer>
  <h3 class="abs disclaimer-title" style="font-weight:400">Disclaimer</h3>
  <p class="abs disclaimer">The material in this web site is provided for enterainment and informational purposes only. Information offered may not be used tio violate the local,state, Regionalor federal laws of any country. You Must consult your loacal authorities for laws that may apply to you. This site does noyt not encourage you to get or engage in gambling.Any useof this information in violation of local ,state ,regional,or federal laws of anyyCountry is prohibited.</p>
  <nav class="abs links" style="left:118px"><a>Home</a><a>Tournaments</a><a>Winners</a><a>Q&amp;A</a><a>Register</a><a>Sign In</a></nav>
  <nav class="abs links" style="left:230px"><a>Win with Demo Accounts</a><a>100% Deposit Bonus</a><a>Guranteed prize Fund</a><a>Earn With friends</a></nav>
  <nav class="abs links" style="left:364px"><a>Tournaments Rules</a><a>Client Agreement</a><a>Privacy</a></nav>
  <nav class="abs links" style="left:495px"><a>About PipArena.com</a><a>Licenses and Documents</a><a>Press Contacts</a><a>Partnership proposal</a></nav>

  <div class="abs cards"><span>Nova</span><span>Orbit</span><span>Pulse</span><span>Crest</span><span>Meridian</span><span>Payly</span></div>
  <div class="abs copyright">Copyright(c) 2011-2013 PipArena.com,All rights reserved</div>
  <div class="abs langs">English  |  español  |  р у с с к и й  |  Indonesia  |  中国的</div>
  <div class="abs follow"><span style="background:#3a5a9a"></span><span style="background:#2aa3e6"></span><span style="background:#1f6fa8"></span><span style="background:#f08a1c"></span></div>
  <div class="abs bottom-strip"></div>
</div>
</body>
</html>
```